Service Plan Sales Flyer

The Watchpost Depot (www.kelvamart.com) is a commercial security integrator that installs security cameras, access control, intrusion, two-way radios and perimeter security. We require a one page flyer for our service plan for new and existing customers. The price of the service plan is $299/yr and includes the following;
1. Discounted service rate of $118/hr
2. Free remote support ($85/hr without a plan)
3. Free remote training
4. Priority support

Please review our brochure attached and create a one page sales flyer with the end goal of having the client sign up for our annual service plan . The plan will automatically renew every year. Email sales@kelvamart.com.

Target Market(s)

commercial industrial clients - no residential

Industry/Entity Type

review our website at www.kelvamart.com

Colors
0054AA
0677BA
7BADD7
CADEEF
E8F1F8
EE7325
F08F49
F5BC92
FAE3D3
FDF4ED

Requirements
Must have
• call to action
Should not have
• too many colors

```html
<!DOCTYPE html>
<html lang="en">
<head>
<meta charset="utf-8">
<title>The Watchpost Depot – Service Plan Flyer</title>
<link href="https://fonts.googleapis.com/css2?family=Bebas+Neue&family=Inter:wght@300;400;500;700;800&display=swap" rel="stylesheet">
<style>
  :root{
    --navy:#0f2d5c;
    --navy-mid:#2c5183;
    --red:#e3141f;
    --red-light:#ef3b3a;
    --page-bg:#a7a8ac;
    --paper:#ffffff;
    --mist:#eef0f3;
  }
  *{box-sizing:border-box;margin:0;padding:0}
  html,body{width:1200px;height:1200px;overflow:hidden;background:var(--page-bg)}
  .flyer{position:absolute;left:228px;top:74px;width:744px;height:1051px;background:var(--paper);overflow:hidden;font-family:"Inter",Arial,sans-serif;color:var(--navy)}
  .hero{position:absolute;left:0;top:0;width:744px;height:431px;background:radial-gradient(circle at 30% 30%,#ffffff 0%,var(--mist) 75%)}
  .brand{position:absolute;left:45px;top:52px;display:flex;align-items:center;gap:12px}
  .brand-dot{width:34px;height:34px;border-radius:50%;background:var(--navy)}
  .brand-name{font-family:"Bebas Neue",sans-serif;font-size:40px;line-height:1;color:var(--navy);letter-spacing:1px}
  .brand-tagline{position:absolute;left:92px;top:96px;font-size:8px;font-weight:700;color:var(--navy)}
  .headline{position:absolute;left:45px;top:156px;font-family:"Bebas Neue",sans-serif;font-size:51px;line-height:43px;color:var(--navy)}
  .headline .accent{color:var(--red)}
  .intro{position:absolute;left:45px;top:260px;font-size:17.5px;line-height:19px;font-weight:500;color:var(--navy);width:400px}
  .intro strong{color:var(--red);font-weight:700}
  .benefits{position:absolute;left:45px;top:322px;list-style:none}
  .benefits li{display:flex;align-items:center;gap:8px;font-size:15px;height:22.4px;color:var(--navy)}
  .benefits li b{color:var(--red);font-weight:700}
  .benefits svg{width:13px;height:13px;flex:none}
  .offer{position:absolute;left:466px;top:0;width:237px;height:476px}
  .offer-text{position:absolute;left:0;top:34px;width:237px;text-align:center;font-family:"Bebas Neue",sans-serif;color:#fff;line-height:1}
  .offer-text .l1{font-size:62px;line-height:50px}
  .offer-text .l2{font-size:62px;line-height:50px}
  .offer-text .l3{font-size:37px;line-height:30px}
  .offer-text .l4{font-size:80px;line-height:64px}
  .offer-photo{position:absolute;left:470px;top:270px;width:236px;height:176px;border-radius:6px;background:radial-gradient(ellipse at 55% 40%,#f4f5f7 0%,#cfd3d9 60%,rgba(200,205,212,0.2) 100%)}
  .section-title{position:absolute;left:45px;font-family:"Bebas Neue",sans-serif;font-size:34px;line-height:1;color:var(--navy);display:flex;align-items:center;gap:6px}
  .section-title span{background:var(--red);color:#fff;padding:3px 18px 1px 14px;clip-path:polygon(10px 0,100% 0,calc(100% - 10px) 100%,0 100%)}
  .services-title{top:480px}
  .why-title{top:816px}
  .cards{position:absolute;left:46px;top:543px;display:flex;gap:8px}
  .card{width:157px;height:229px;border-radius:8px 8px 0 0;padding:12px 10px;color:#fff}
  .card.navy{background:linear-gradient(180deg,var(--navy-mid),#1e3c6b)}
  .card.red{background:linear-gradient(180deg,var(--red),var(--red-light))}
  .card-icon{width:45px;height:45px;border:2px solid #fff;border-radius:50%;display:flex;align-items:center;justify-content:center}
  .card-icon svg{width:24px;height:24px}
  .card h3{margin-top:10px;font-size:14px;line-height:14px;font-weight:700;text-transform:uppercase}
  .card p{margin-top:12px;font-size:12.3px;line-height:15px;font-weight:300}
  .why-text{position:absolute;left:43px;top:866px;width:660px;font-size:15.3px;line-height:20px;font-weight:300;color:var(--navy)}
  .footer{position:absolute;left:0;top:980px;width:744px;height:71px;background:linear-gradient(90deg,var(--navy),#2f4f80)}
  .footer-cta{position:absolute;left:0;top:0;width:272px;height:71px;background:linear-gradient(90deg,var(--red),var(--red-light));clip-path:polygon(0 0,100% 0,calc(100% - 24px) 100%,0 100%)}
  .footer-cta h2{position:absolute;left:43px;top:16px;font-family:"Bebas Neue",sans-serif;font-size:36px;line-height:1;color:#fff;font-weight:400}
  .contact{position:absolute;top:19px;display:flex;align-items:center;gap:9px;color:#fff}
  .contact svg{width:24px;height:24px}
  .contact small{display:block;font-size:7px;line-height:8px;font-weight:300}
  .contact strong{display:block;font-size:15.5px;line-height:18px;font-weight:700}
  .contact-web{left:291px}
  .contact-phone{left:527px}
  .divider{position:absolute;left:513px;top:24px;width:1px;height:22px;background:var(--red)}
</style>
</head>
<body>
<main class="flyer">
  <section class="hero">
    <div class="brand">
      <div class="brand-dot"></div>
      <div class="brand-name">The Watchpost Depot</div>
    </div>
    <div class="brand-tagline">Commercial &amp; Industrial Solutions</div>

    <h1 class="headline">Maximize your security<br><span class="accent">with our service plan!</span></h1>

    <p class="intro">Unleash the power of enhanced security with our <strong>$299/yr membership.</strong></p>

    <ul class="benefits">
      <li><svg viewBox="0 0 14 14"><circle cx="7" cy="7" r="6" fill="none" stroke="#e3141f" stroke-width="1.4"/><path d="M4 7.2l2.2 2.2L11 4" fill="none" stroke="#e3141f" stroke-width="1.6"/></svg>Discounted service rate of&nbsp;<b>$118/hr</b></li>
      <li><svg viewBox="0 0 14 14"><circle cx="7" cy="7" r="6" fill="none" stroke="#e3141f" stroke-width="1.4"/><path d="M4 7.2l2.2 2.2L11 4" fill="none" stroke="#e3141f" stroke-width="1.6"/></svg>Free remote support&nbsp;<b>($85/hr without a plan)</b></li>
      <li><svg viewBox="0 0 14 14"><circle cx="7" cy="7" r="6" fill="none" stroke="#e3141f" stroke-width="1.4"/><path d="M4 7.2l2.2 2.2L11 4" fill="none" stroke="#e3141f" stroke-width="1.6"/></svg>Free remote training</li>
      <li><svg viewBox="0 0 14 14"><circle cx="7" cy="7" r="6" fill="none" stroke="#e3141f" stroke-width="1.4"/><path d="M4 7.2l2.2 2.2L11 4" fill="none" stroke="#e3141f" stroke-width="1.6"/></svg>Priority support</li>
    </ul>
  </section>

  <aside class="offer">
    <svg width="237" height="476" viewBox="0 0 237 476">
      <defs>
        <radialGradient id="offerRed" cx="50%" cy="35%" r="70%">
          <stop offset="0" stop-color="#f0403c"/>
          <stop offset="1" stop-color="#e3141f"/>
        </radialGradient>
      </defs>
      <rect width="237" height="476" fill="url(#offerRed)"/>
      <polygon points="0,420 237,366 237,439 0,476" fill="#2c4a7e"/>
    </svg>
    <div class="offer-text">
      <div class="l1">Unlock</div>
      <div class="l2">Exclusive</div>
      <div class="l3">Benefits for only</div>
      <div class="l4">$299/yr</div>
    </div>
  </aside>
  <div class="offer-photo" role="img" aria-label="Product photo of a video management monitor with a dome camera and a bullet camera"></div>

  <h2 class="section-title services-title">Our <span>Services</span></h2>

  <div class="cards">
    <article class="card navy">
      <div class="card-icon"><svg viewBox="0 0 24 24" fill="none" stroke="#fff" stroke-width="1.6"><circle cx="15" cy="9" r="3.5"/><path d="M12.5 11.5L5 19M7 17l2 2M9 15l2 2"/><path d="M3 3l18 18"/></svg></div>
      <h3>Access Control<br>&amp; Intercom</h3>
      <p>Integrate intrusion, video surveillance, and card credential control for seamless security management from any device.</p>
    </article>
    <article class="card red">
      <div class="card-icon"><svg viewBox="0 0 24 24" fill="none" stroke="#fff" stroke-width="1.6"><rect x="6" y="3" width="12" height="18" rx="1.5"/><rect x="8.5" y="5.5" width="7" height="3"/><path d="M9 12h1M12 12h1M15 12h0M9 15h1M12 15h1M9 18h1M12 18h1"/></svg></div>
      <h3>Access Control<br>&amp; Intercom</h3>
      <p>Integrate intrusion, video surveillance, and card credential control for seamless security management from any device.</p>
    </article>
    <article class="card navy">
      <div class="card-icon"><svg viewBox="0 0 24 24" fill="none" stroke="#fff" stroke-width="1.4"><path d="M3 8h18M3 13h18M3 18h18M6 6v14M10 6v14M14 6v14M18 6v14"/></svg></div>
      <h3>Perimeter<br>Security</h3>
      <p>Notify security personnel of intruders with our fence vibration sensors and/or our video analytics detecting humans and vehicles.</p>
    </article>
    <article class="card red">
      <div class="card-icon"><svg viewBox="0 0 24 24" fill="none" stroke="#fff" stroke-width="1.6"><rect x="6" y="9" width="13" height="6" rx="1" transform="rotate(-20 12 12)"/><path d="M4 17v4M4 19h4M12 8V4"/></svg></div>
      <h3>Surveillance<br>Cameras</h3>
      <p>Enhance Security with User-Friendly Video Management Software: Ultra-High Definition, Analytics, Quick Retrieval.</p>
    </article>
  </div>

  <h2 class="section-title why-title">Why <span>Choose us?</span></h2>
  <p class="why-text">Choose The Watchpost Depot as your trusted partner for comprehensive security solutions. With our experience, expert team, and reliable partnerships, we deliver exceptional results that exceed your expectations. Rest assured that your security needs are in the hands of professionals dedicated to providing you with the highest level of service and security.</p>

  <footer class="footer">
    <div class="footer-cta"><h2>Contact us today!</h2></div>
    <div class="contact contact-web">
      <svg viewBox="0 0 24 24" fill="none" stroke="#fff" stroke-width="1.3"><circle cx="12" cy="12" r="10"/><ellipse cx="12" cy="12" rx="4.5" ry="10"/><path d="M2 12h20M4 7h16M4 17h16"/></svg>
      <div><small>Website</small><strong>WWW.KELVAMART.COM</strong></div>
    </div>
    <div class="divider"></div>
    <div class="contact contact-phone">
      <svg viewBox="0 0 24 24" fill="none" stroke="#fff" stroke-width="1.3"><circle cx="12" cy="12" r="10.5"/><path d="M8.5 6.5l2 2.5-1.2 1.5c.8 1.8 2.2 3.2 4 4l1.5-1.2 2.5 2-1 2c-4.5 0-9.3-4.8-9.3-9.3z"/></svg>
      <div><small>Toll Free</small><strong>1-877-555-0142</strong></div>
    </div>
  </footer>
</main>
</body>
</html>
```